Web Design Project

I am looking for a simple website to promote my business called Wyllard Benick Consulting. We provide consulting and implementation services for finance and supply chain processes and systems.

We want to project a professional but innovative image. I have attached a copy of our logo. It is not necessary to stick with the colours in the logo - we encourage you to experiment with the colours and even to change the colours of the logo to fit with your design. Although, on the front page we would like to have the logo with its original colours.

Required sections:
About
What we do
Clients
Contact
Updates

Target Market(s)

Medium to large companies including multi-nationals in all industries.

Industry/Entity Type

Finance

Requirements
Must have
• Required sections:
About
What we do
Clients
Contact

```html
<!DOCTYPE html>
<html lang="en">
<head>
<meta charset="utf-8">
<title>Wyllard Benick Consulting</title>
<link rel="stylesheet" href="https://fonts.googleapis.com/css2?family=Mulish:wght@400;600;700;800&family=Questrial&family=Arimo:wght@400&display=swap">
<style>
  :root {
    --blue: #0b5aa8;
    --blue-dark: #084a8c;
    --green: #8aab1a;
    --green-light: #a9c427;
    --green-text: #8fa81c;
    --grey-text: #666;
    --body-text: #6e6e6e;
    --rule: #cfcfcf;
    --nav-text: #555;
    --footer-bg: #000;
    --footer-text: #bdbdbd;
    --hero-ink: #1b1b1b;
  }
  * { margin: 0; padding: 0; box-sizing: border-box; }
  html, body { width: 1105px; height: 1200px; overflow: hidden; background: #fff; }
  .page { position: relative; width: 1105px; height: 1200px; overflow: hidden; font-family: "Arimo", Arial, sans-serif; }

  .top-strip { position: absolute; left: 0; top: 0; width: 100%; height: 5px; background: linear-gradient(#555, #888); }
  .site-header { position: absolute; left: 0; top: 5px; width: 100%; height: 115px; background: linear-gradient(#f4f4f4, #fff 30%); border-bottom: 1px solid #ddd; }
  .brand { position: absolute; left: 110px; top: 26px; display: flex; align-items: center; gap: 10px; color: var(--blue); font-family: "Mulish", sans-serif; font-weight: 700; }
  .brand-mark { width: 44px; height: 44px; border-radius: 50%; background: var(--green-light); flex: none; }
  .brand-name { font-size: 16px; line-height: 19px; letter-spacing: .3px; }
  .brand-name small { display: block; font-size: 12px; letter-spacing: .8px; font-weight: 700; }

  .main-nav { position: absolute; top: 43px; left: 490px; display: flex; align-items: center; font-family: "Mulish", sans-serif; font-weight: 700; font-size: 15px; color: var(--nav-text); }
  .main-nav a { color: inherit; text-decoration: none; letter-spacing: .3px; }
  .main-nav .active { width: 103px; height: 33px; border-radius: 17px; background: linear-gradient(#2a86dc, var(--blue-dark)); color: #fff; display: flex; align-items: center; justify-content: center; box-shadow: 0 1px 3px rgba(0,0,0,.4); }
  .nav-what { margin-left: 38px; }
  .nav-clients { margin-left: 62px; }
  .nav-contact { margin-left: 62px; }

  .hero { position: absolute; left: 0; top: 120px; width: 100%; height: 404px; background: linear-gradient(100deg, #e9e9ed 0%, #dcdde2 45%, #eeeef0 75%, #e4e4e6 100%); }
  .hero-text { position: absolute; left: 110px; top: 98px; width: 380px; }
  .hero-title { font-family: "Mulish", sans-serif; font-weight: 800; font-size: 50px; line-height: 55px; color: var(--blue); letter-spacing: .5px; }
  .hero-copy { margin-top: 16px; font-family: "Mulish", sans-serif; font-size: 17.5px; line-height: 22px; color: var(--hero-ink); text-align: justify; }
  .slider-dots { position: absolute; left: 124px; top: 381px; display: flex; gap: 27px; }
  .slider-dots span { width: 10px; height: 10px; border-radius: 50%; background: radial-gradient(circle at 40% 35%, #fff, #aaa); box-shadow: 0 1px 2px rgba(0,0,0,.3); }
  .slider-dots span.on { background: radial-gradient(circle at 40% 35%, #fff, #ddd); }

  .features { position: absolute; top: 551px; left: 110px; display: flex; gap: 27px; }
  .feature { position: relative; width: 276px; height: 156px; background: radial-gradient(ellipse at 50% 30%, var(--green-light), var(--green) 75%); color: #fff; text-align: center; }
  .feature::after { content: ""; position: absolute; left: 18px; right: 18px; bottom: -16px; height: 16px; background: radial-gradient(ellipse at 50% 0, rgba(0,0,0,.28), transparent 70%); }
  .feature svg { margin-top: 12px; height: 42px; }
  .feature h3 { font-family: "Questrial", sans-serif; font-weight: 400; font-size: 22px; margin-top: 5px; letter-spacing: .5px; }
  .feature p { font-size: 10.7px; line-height: 13.5px; margin: 9px 16px 0; }

  .section-title { position: absolute; top: 752px; font-family: "Questrial", sans-serif; font-size: 17.5px; color: var(--grey-text); letter-spacing: .3px; padding-bottom: 14px; border-bottom: 1px solid var(--rule); }
  .what-title { left: 110px; width: 580px; }
  .how-title { left: 717px; width: 278px; }

  .what-photo { position: absolute; left: 110px; top: 808px; width: 277px; height: 163px; border: 4px solid #ddd; background: linear-gradient(120deg, #a9c8d2, #d4e2e6 50%, #8ea7b1); }
  .what-copy { position: absolute; left: 396px; top: 806px; width: 294px; font-size: 10.6px; line-height: 15.6px; color: var(--body-text); text-align: justify; }
  .what-copy .lead { color: var(--green-text); font-size: 11.5px; margin-bottom: 15px; text-align: left; }
  .how-copy { position: absolute; left: 717px; top: 806px; width: 278px; font-size: 10.6px; line-height: 16.5px; color: var(--body-text); text-align: justify; }
  .how-copy .lead { font-size: 11.5px; }
  .how-copy p + p { margin-top: 16px; }

  .clients { position: absolute; left: 110px; top: 1013px; width: 885px; height: 83px; border: 1px solid #d4d4d4; display: flex; align-items: center; justify-content: space-around; font-family: "Mulish", sans-serif; font-weight: 800; font-size: 24px; color: #444; }

  .site-footer { position: absolute; left: 0; top: 1122px; width: 100%; height: 78px; background: var(--footer-bg); }
  .copyright { position: absolute; left: 104px; top: 32px; font-size: 11.8px; color: var(--footer-text); }
  .social { position: absolute; left: 853px; top: 25px; display: flex; gap: 8px; }
  .social a { width: 29px; height: 29px; background: #2b2b2b; color: #ddd; font-size: 10px; font-family: "Arimo", sans-serif; display: flex; align-items: center; justify-content: center; text-decoration: none; }
</style>
</head>
<body>
<div class="page">
  <div class="top-strip"></div>
  <header class="site-header">
    <div class="brand">
      <span class="brand-mark"></span>
      <span class="brand-name">WYLLARD BENICK<small>CONSULTING LIMITED</small></span>
    </div>
    <nav class="main-nav">
      <a class="active" href="#">ABOUT</a>
      <a class="nav-what" href="#">WHAT WE DO</a>
      <a class="nav-clients" href="#">CLIENTS</a>
      <a class="nav-contact" href="#">CONTACT</a>
    </nav>
  </header>

  <section class="hero" role="img" aria-label="Businessman pushing a large white jigsaw puzzle piece into place">
    <div class="hero-text">
      <h1 class="hero-title">IMPLEMENTATION SERVICES</h1>
      <p class="hero-copy">Sed ut perspiciatis unde omnis iste natus error sit voluptatem accusantium doloremque laudantium, totam rem aperiam, eaque ipsa quae ab illo inventore veritatis et quasi...</p>
    </div>
    <div class="slider-dots"><span class="on"></span><span></span><span></span></div>
  </section>

  <section class="features">
    <article class="feature">
      <svg viewBox="0 0 40 42" width="40" aria-hidden="true"><path d="M6 38 C4 18 18 4 36 4 C36 24 24 36 6 38 Z" fill="#fff"/><path d="M8 36 L30 10 M16 27 L16 20 M22 20 L28 20 M12 31 L20 31" stroke="#9bb822" stroke-width="2" fill="none"/></svg>
      <h3>OUR VISION</h3>
      <p>Sed ut perspiciatis unde omnis iste natus error sit voluptatem accusantium doloremque laudantium, totam rem aperiam, eaque ipsa</p>
    </article>
    <article class="feature">
      <svg viewBox="0 0 40 42" width="40" aria-hidden="true"><path d="M11 4 H29 V16 C29 22 25 26 20 26 C15 26 11 22 11 16 Z" fill="#fff"/><path d="M11 8 H5 C5 16 9 19 13 19 M29 8 H35 C35 16 31 19 27 19" stroke="#fff" stroke-width="3" fill="none"/><rect x="18" y="26" width="4" height="7" fill="#fff"/><rect x="12" y="33" width="16" height="6" fill="#fff"/></svg>
      <h3>OUR GOAL</h3>
      <p>Sed ut perspiciatis unde omnis iste natus error sit voluptatem accusantium doloremque laudantium, totam rem aperiam, eaque ipsa</p>
    </article>
    <article class="feature">
      <svg viewBox="0 0 40 42" width="40" aria-hidden="true"><path d="M20 2 C11 2 6 8 6 15 C6 22 13 25 14 31 H26 C27 25 34 22 34 15 C34 8 29 2 20 2 Z" fill="#fff"/><rect x="14" y="33" width="12" height="3" fill="#fff"/><rect x="15" y="38" width="10" height="3" rx="1.5" fill="#fff"/></svg>
      <h3>SOLUTION</h3>
      <p>Sed ut perspiciatis unde omnis iste natus error sit voluptatem accusantium doloremque laudantium, totam rem aperiam, eaque ipsa</p>
    </article>
  </section>

  <h2 class="section-title what-title">WHAT WE DO</h2>
  <h2 class="section-title how-title">HOW IT WORKS</h2>

  <div class="what-photo" role="img" aria-label="Two colleagues reviewing documents at a meeting table"></div>
  <div class="what-copy">
    <p class="lead">Sed ut perspiciatis unde omnis iste natus error sit voluptatem accusantium doloremque laudantium,</p>
    <p>totam rem aperiam, eaque ipsa quae ab illo inventore veritatis et quasi architecto beatae vitae dicta sunt explicabo. Nemo enim ipsam voluptatem quia voluptas sit aspernatur aut odit aut fugit, sed quia consequuntur magni dolores eos qui ratione voluptatem sequi nesciunt. Neque porro quisquam est, qui dolorem ipsum quia dolor sit amet, consectetur, adipisci velit, sed quia non numquam eius modi tempora incidunt ut labore et dolore magnam aliquam quae-</p>
  </div>
  <div class="how-copy">
    <p class="lead">Sed ut perspiciatis unde omnis iste natus error sit voluptatem accusam doloremque laudantium,tam rem aperiam, eaque ipsa quae ab illo inventore</p>
    <p>veritatis et quasi architecto beatae vitae dicta sunt explicabo. Nemo enim ipsam voluptatem quia voluptas sit aspernatur aut odit aut fugit, sed quia consequuntur magni dolores eos qui ratione voluptatem sequi nesciunt. Neque porro quisquam est, qui dolorem ipsum quia dolor sit amet, consectetur, adipisci velit, sed quia non</p>
  </div>

  <section class="clients" aria-label="Clients">
    <span>Corvalen</span>
    <span>Tradewick</span>
    <span>Arkemo</span>
    <span>Searlox</span>
    <span>Hoshimaru</span>
    <span>Veyla</span>
  </section>

  <footer class="site-footer">
    <p class="copyright">© 2013 Wyllard Benick Consulting.. | All rights reserved.</p>
    <div class="social">
      <a href="#">Fn</a><a href="#">Ch</a><a href="#">Vd</a><a href="#">Px</a>
    </div>
  </footer>
</div>
</body>
</html>
```